Plakat-Design für Verkauf von Bio-zertifiziertem Saatgut
Zielgruppe
Wir sind ein Start Up und verkaufen BIO Zertifiziertes Saatgut für Gemüse, Kräuter, Heilpflanzen und essbare Sprossen etc. Zielgruppe ist vor allem die DIY Community von Jung bis Alt.
Aufgabenstellung
*** INFO*** Da es keine 'Kalender'-Projekte gibt, sollten wir das Projekt unter 'Plakat' einstellen ***INFO***
Wir sind auf der Suche nach einem Design für einen Monatskalender (Deckblatt, 12 Monate, Schlussblatt) der als ewiger Aussaatkalender fungieren soll (Keine Jahreszahlen, nur der Monat). Jeden Monat sollen die Sorten gezeigt werden die jetzt ausgesät werden können. Am Besten teilweise (nicht alle) als Illustrationen oder Bilder. Die Sorten orientieren sich an unserem Saatgutsortiment. Als Unterteilung kann man: 'Vorzucht im Haus', Frühbeet' und 'Direktsaat'
Die Informationen welche Samen wann ausgesät werden, kommen von uns. (Erstmal Platzhalter für das Design nutzen) Falls der Designer Erfahrung in diesem Bereich hat, kann er die Informationen auch selber einfügen. Sonst ist der Designer für Layout und Illustrationen/Bilder zuständig. Toll wäre wenn für jeden Monat noch eine 'Bauernweisheit' zum Thema Pflanzen / Aussaat / Garten hinzugefügt werden kann.
Das Design soll sich an unserer CI der Website www.keimwerk-lutra.de orientieren. Logo, Farben und Fonts (My-Everything, BW Mitga) sind im Anhang beigefügt. Auch die Vorlage der Druckerei ist beigefügt. Format: DIN A4 hoch (210 x 297 mm), beidseitig bedruckt so das man den Kalender auch Aufgeklappt nutzen kann.
Falls noch Informationen benötigt werden, dann meldet euch gerne!

```html
<!DOCTYPE html>
<html lang="de">
<head>
<meta charset="utf-8">
<title>Keimwerk Lutra – Ewiger Aussaatkalender</title>
<link rel="stylesheet" href="https://fonts.googleapis.com/css2?family=Allura&family=Caveat:wght@500&family=Montserrat:wght@400;700;800&display=swap">
<style>
  :root {
    --stage: #45413e;
    --paper: #f4f5f1;
    --band: #e6ede0;
    --brand-green: #5f8a3c;
    --text-brown: #6b4a2a;
    --ink: #2e2a25;
    --vorzucht: #e8a868;
    --fruehbeet: #a8cc88;
    --direktsaat: #6b4a1e;
    --badge-green: #9ac43a;
    --slate: #4a4845;
  }
  * { box-sizing: border-box; margin: 0; padding: 0; }
  html, body { width: 1200px; height: 800px; overflow: hidden; }
  body {
    background: var(--stage);
    font-family: "Montserrat", Arial, sans-serif;
    position: relative;
  }
  .page { position: absolute; width: 440px; height: 624px; top: 93px; overflow: hidden; }

  /* Cover */
  .cover { left: 110px; background: var(--paper); }
  .cover-header {
    position: absolute; left: 0; top: 0; width: 100%; height: 118px;
    background: linear-gradient(180deg, #f3f3f0, #e4e6df);
    display: flex; align-items: center; justify-content: center; gap: 10px;
  }
  .brand-dot { width: 14px; height: 14px; border-radius: 50%; background: var(--brand-green); }
  .brand-name { font-weight: 700; color: var(--brand-green); letter-spacing: 2px; font-size: 17px; }
  .cover-photo {
    position: absolute; left: 0; top: 118px; width: 100%; height: 506px;
    background:
      radial-gradient(ellipse 90px 150px at 58% 58%, #9bbf5a 0%, rgba(120,160,60,0.5) 55%, transparent 80%),
      radial-gradient(ellipse 70px 60px at 75% 90%, #8fb24f 0%, transparent 75%),
      linear-gradient(180deg, #7c7f78 0%, #4a4b47 35%, #2c2c2a 70%, #3b3a37 100%);
  }
  .cover-title {
    position: absolute; left: 0; width: 100%; top: 215px; text-align: center;
    font-family: "Allura", cursive; font-weight: 400; color: #fff; font-size: 44px;
    white-space: nowrap; transform: rotate(-6deg);
  }
  .organic-badge { position: absolute; }

  /* March page */
  .month { left: 677px; background: #556b3e; }
  .soil-strip {
    position: absolute; left: 0; top: 0; width: 100%; height: 35px;
    background: linear-gradient(90deg, #4a3628, #6a4c35 40%, #3e2e22 70%, #5c4a37);
  }
  .todo-band {
    position: absolute; left: 0; top: 35px; width: 100%; height: 104px; background: var(--band);
  }
  .todo-title { position: absolute; left: 16px; top: 14px; font-weight: 800; font-size: 10px; color: var(--ink); letter-spacing: .3px; }
  .veg-row {
    position: absolute; left: 18px; top: 30px; width: 220px; height: 68px; border-radius: 6px;
    background: linear-gradient(90deg, #dfe9d4, #efe2d4, #e7dcd9, #dfe9d4);
  }
  .todo-brand { position: absolute; right: 22px; top: 40px; display: flex; align-items: center; gap: 8px; }
  .todo-brand .brand-name { font-size: 15px; }
  .garden-photo {
    position: absolute; left: 0; top: 139px; width: 100%; height: 485px;
    background:
      radial-gradient(ellipse 110px 200px at 78% 72%, #8a5a3a 0%, rgba(120,70,40,.4) 50%, transparent 80%),
      linear-gradient(180deg, #6d7b4f 0%, #56703a 45%, #44592d 75%, #5b4a33 100%);
  }
  .sow-column {
    position: absolute; top: 155px; width: 122px; height: 230px;
    background: rgba(245,238,226,0.78); border: 4px solid; padding: 11px 6px;
  }
  .sow-column.vorzucht { left: 19px; border-color: var(--vorzucht); }
  .sow-column.fruehbeet { left: 157px; border-color: var(--fruehbeet); background: rgba(236,242,228,0.78); }
  .sow-column.direktsaat { left: 296px; border-color: var(--direktsaat); }
  .sow-list { list-style: none; }
  .sow-item {
    display: flex; align-items: center; gap: 6px; height: 18.5px;
    font-size: 8.5px; color: var(--text-brown); white-space: nowrap;
  }
  .veg-icon { width: 20px; height: 12px; border-radius: 6px; flex: none; }
  .marker { margin-left: auto; width: 9px; height: 9px; flex: none; }
  .month-name {
    position: absolute; left: 26px; top: 392px;
    font-family: "Allura", cursive; font-weight: 400; color: #fff; font-size: 52px; transform: rotate(-10deg);
  }
  .good-to-know {
    position: absolute; left: 21px; top: 462px; width: 157px; height: 143px;
    background: #eef2ea; padding: 8px 8px 0 10px;
  }
  .gtk-title { font-weight: 800; font-size: 9.5px; color: var(--ink); margin-bottom: 4px; }
  .legend-row { display: flex; align-items: center; gap: 10px; height: 16px; font-size: 7.5px; color: var(--text-brown); letter-spacing: .6px; white-space: nowrap; }
  .swatch { width: 29px; height: 9px; flex: none; }
  .symbol-row { display: flex; align-items: center; gap: 5px; height: 12px; font-size: 7px; color: var(--ink); white-space: nowrap; }
  .symbol-row.first { margin-top: 5px; }
  .symbol-row svg { flex: none; }
  .gtk-claim { position: absolute; left: 10px; top: 107px; width: 140px; }
  .gtk-claim strong { display: block; font-size: 6.2px; font-weight: 700; color: var(--ink); margin-bottom: 2px; white-space: nowrap; }
  .gtk-claim p { font-size: 5.2px; line-height: 1.3; color: var(--ink); width: 92px; }
  .slate-quote {
    position: absolute; left: 334px; top: 513px; width: 104px; height: 115px;
    background: radial-gradient(ellipse at 40% 30%, #5c5a56, var(--slate) 60%, #3a3835);
    border-radius: 40px 30px 0 10px;
    display: flex; align-items: center; justify-content: center; text-align: center;
    font-family: "Caveat", cursive; color: #f2f0ea; font-size: 13px; line-height: 1.15;
    padding: 8px 6px 14px;
  }
</style>
</head>
<body>

  <section class="page cover">
    <header class="cover-header">
      <span class="brand-dot"></span>
      <span class="brand-name">KEIMWERK LUTRA</span>
    </header>
    <div class="cover-photo" role="img" aria-label="Foto: junge grüne Keimlinge wachsen aus dunkler Erde"></div>
    <h1 class="cover-title">Ewiger Aussaatkalender</h1>
    <svg class="organic-badge" style="left:12px; top:560px" width="78" height="60" viewBox="0 0 78 60" aria-hidden="true">
      <path d="M8 10 C20 -2 34 4 38 14 C44 4 62 0 74 12 C78 30 58 48 36 58 C18 50 2 32 8 10 Z" fill="#8cbf55" opacity=".9"/>
    </svg>
  </section>

  <section class="page month">
    <div class="soil-strip" role="img" aria-label="Foto: Gartenerde mit Laub"></div>
    <header class="todo-band">
      <h2 class="todo-title">TO DO LIST</h2>
      <div class="veg-row" role="img" aria-label="Illustrationen: Gemüsesorten wie Möhre, Sellerie, Tomaten, Kohl, Zucchini, Radieschen, Zwiebel und Erbsen"></div>
      <div class="todo-brand">
        <span class="brand-dot"></span>
        <span class="brand-name">KEIMWERK LUTRA</span>
      </div>
    </header>

    <div class="garden-photo" role="img" aria-label="Foto: Kind mit Mütze gräbt im herbstlichen Gemüsegarten"></div>

    <div class="sow-column vorzucht">
      <ul class="sow-list">
        <li class="sow-item"><span class="veg-icon" style="background:#d9566a" role="img" aria-label="Illustration Radieschen"></span>Radieschen</li>
        <li class="sow-item"><span class="veg-icon" style="background:#e8893a" role="img" aria-label="Illustration Möhre"></span>Frühe Möhre
          <svg class="marker" viewBox="0 0 10 10" aria-label="Vorkeimen"><path d="M5 10 V5 M5 5 C5 2 3 1 2 1 M5 5 C5 3 7 2 8 3" stroke="#222" stroke-width="1.3" fill="none"/></svg></li>
        <li class="sow-item"><span class="veg-icon" style="background:#7fae4a" role="img" aria-label="Illustration Zuckererbse"></span>Zuckererbse
          <svg class="marker" viewBox="0 0 10 10" aria-label="Lichtkeimer"><circle cx="5" cy="5" r="2.6" fill="#111"/><path d="M5 0v1.5M5 8.5V10M0 5h1.5M8.5 5H10M1.5 1.5l1 1M7.5 7.5l1 1M1.5 8.5l1-1M7.5 2.5l1-1" stroke="#111"/></svg></li>
        <li class="sow-item"><span class="veg-icon" style="background:#9cc560" role="img" aria-label="Illustration Weißkohl"></span>Weißkohl</li>
        <li class="sow-item"><span class="veg-icon" style="background:#8bbf55" role="img" aria-label="Illustration Stangensellerie"></span>Stangenellerie</li>
      </ul>
    </div>
    <div class="sow-column fruehbeet">
      <ul class="sow-list">
        <li class="sow-item"><span class="veg-icon" style="background:#4f8a3a" role="img" aria-label="Illustration Spinat"></span>Spinat</li>
        <li class="sow-item"><span class="veg-icon" style="background:#9a2b3e" role="img" aria-label="Illustration Rote Bete"></span>Rote Bete</li>
        <li class="sow-item"><span class="veg-icon" style="background:#5e9a45" role="img" aria-label="Illustration Rucola"></span>Rucola</li>
      </ul>
    </div>
    <div class="sow-column direktsaat">
      <ul class="sow-list">
        <li class="sow-item"><span class="veg-icon" style="background:#a64a8a" role="img" aria-label="Illustration Steckzwiebel"></span>Steckzwiebel
          <svg class="marker" viewBox="0 0 10 10" aria-label="Vorkeimen"><path d="M5 10 V5 M5 5 C5 2 3 1 2 1 M5 5 C5 3 7 2 8 3" stroke="#222" stroke-width="1.3" fill="none"/></svg></li>
        <li class="sow-item"><span class="veg-icon" style="background:#5b2d6b" role="img" aria-label="Illustration Aubergine"></span>Aubergine
          <svg class="marker" viewBox="0 0 10 10" aria-label="Lichtkeimer"><circle cx="5" cy="5" r="2.6" fill="#111"/><path d="M5 0v1.5M5 8.5V10M0 5h1.5M8.5 5H10M1.5 1.5l1 1M7.5 7.5l1 1M1.5 8.5l1-1M7.5 2.5l1-1" stroke="#111"/></svg></li>
        <li class="sow-item"><span class="veg-icon" style="background:#7ea54a" role="img" aria-label="Illustration Spargel"></span>Spargel</li>
        <li class="sow-item"><span class="veg-icon" style="background:#cfe3b0" role="img" aria-label="Illustration Fenchel"></span>Fenchel</li>
      </ul>
    </div>

    <h2 class="month-name">März</h2>

    <aside class="good-to-know">
      <h3 class="gtk-title">GOOD TO KNOW</h3>
      <div class="legend-row"><span class="swatch" style="background:var(--vorzucht)"></span>VORZUCHT IM HAUS</div>
      <div class="legend-row"><span class="swatch" style="background:var(--fruehbeet)"></span>FRÜHBEET</div>
      <div class="legend-row"><span class="swatch" style="background:var(--direktsaat)"></span>DIREKTSAAT</div>
      <div class="symbol-row first">
        <svg width="9" height="9" viewBox="0 0 10 10" aria-hidden="true"><path d="M5 10 V5 M5 5 C5 2 3 1 2 1 M5 5 C5 3 7 2 8 3" stroke="#222" stroke-width="1.3" fill="none"/></svg>
        Anpflanzung erfordert Vorkeimen</div>
      <div class="symbol-row">
        <svg width="9" height="9" viewBox="0 0 10 10" aria-hidden="true"><circle cx="5" cy="5" r="2.6" fill="#111"/><path d="M5 0v1.5M5 8.5V10M0 5h1.5M8.5 5H10M1.5 1.5l1 1M7.5 7.5l1 1M1.5 8.5l1-1M7.5 2.5l1-1" stroke="#111"/></svg>
        Lichtkeimer</div>
      <div class="gtk-claim">
        <strong>Pflanzen mit grünem Gewissen</strong>
        <p>BIO-Zertifikat, welches gewährleistet, dass das Saatgut den höchsten Qualitätsstandards entspricht.</p>
      </div>
    </aside>
    <svg class="organic-badge" style="left:182px; top:550px" width="62" height="56" viewBox="0 0 66 60" aria-hidden="true">
      <path d="M6 8 C16 -2 30 2 33 12 C38 2 54 0 63 12 C66 30 50 46 30 58 C14 50 0 32 6 8 Z" fill="var(--badge-green)"/>
    </svg>

    <blockquote class="slate-quote">Fürchte nicht den Schnee im März, darunter schlägt ein warmes Herz.</blockquote>
  </section>

</body>
</html>
```